Powerpoint Template Background Design

We are looking to update our powerpoint background to align better with our recently updated logo. I've included our current logo (BankGothic Md BT Medium) and previous ppt background we had used for reference. Page orientation should be landscape. Should be usable online and as a printable deck. We are in the digital advertising sales industry and represent various digital ad products to ad agencies and clients who are interested in marketing their products using mobile advertising tools. the RGB color yellow in our logo is 245, 191,34 #fsbf22. We like to also see the grey and black in our logo included. We'd like it to be similar but new and refreshed from our previous ppt background. I've added our current sales deck for your review and consideration with your design.

Target Market(s)

Advertisers, Ad agencies

Industry/Entity Type

Advertising

Colors
ffc214

Requirements
Must have
• Include Logo. Preferably our 3d logo on the cover page. color scheme should match our logo. Must have cover page and template border page that we will use throughout the entire presentation.
Nice to have
• Full cover page graphic using our 3d logo and allows us to add text in a fixed area of the slide
Should not have
• If recommending full slide color/imagery please note it will be used both online and as a printable deck. Do not include the tagline and/or text from the previously used presentation template.

```html
<!DOCTYPE html>
<html lang="en">
<head>
<meta charset="utf-8">
<title>Northpeak Interactive Media – Presentation Cover</title>
<link href="https://fonts.googleapis.com/css2?family=Fira+Sans+Condensed:wght@500&family=Open+Sans:wght@400;600&family=Montserrat:wght@400;600&display=swap" rel="stylesheet">
<style>
  :root {
    --page-bg: #e0e1e3;
    --slide-bg: #ffffff;
    --band-dark: #4a5361;
    --accent-yellow: #f5bf22;
    --rule-grey: #8c9098;
    --ink: #1e1e1e;
    --muted-ink: #555a61;
  }
  * { margin: 0; padding: 0; box-sizing: border-box; }
  html, body {
    width: 900px; height: 1200px; overflow: hidden;
    background: var(--page-bg);
  }
  .canvas { position: relative; width: 900px; height: 1200px; }
  .slide {
    position: absolute; left: 92px; width: 720px; height: 406px;
    background: var(--slide-bg); overflow: hidden;
  }
  .slide--media { top: 167px; }
  .slide--touch { top: 619px; }
  .slide__band { position: absolute; left: 0; top: 0; width: 720px; height: 320px; }
  .brand {
    position: absolute; left: 72px; top: 98px;
    display: flex; align-items: center; gap: 8px;
  }
  .brand__dot { width: 12px; height: 12px; border-radius: 50%; background: var(--accent-yellow); }
  .brand__name {
    font-family: "Montserrat", sans-serif; font-weight: 600;
    font-size: 20px; letter-spacing: 3px; color: var(--ink);
  }
  .brand__sub {
    position: absolute; left: 72px; top: 124px;
    font-family: "Montserrat", sans-serif; font-weight: 600;
    font-size: 8px; letter-spacing: 3.2px; color: var(--ink);
  }
  .cover-title {
    position: absolute; right: 38px; top: 176px; text-align: right;
  }
  .cover-title__welcome {
    font-family: "Fira Sans Condensed", sans-serif; font-weight: 500;
    font-size: 35px; line-height: 1; color: var(--accent-yellow);
  }
  .cover-title__sub {
    margin-top: 8px;
    font-family: "Montserrat", sans-serif; font-weight: 400;
    font-size: 17px; letter-spacing: 3.6px; color: #ffffff;
  }
  .cover-title__date {
    margin-top: 8px;
    font-family: "Open Sans", sans-serif; font-weight: 400;
    font-size: 13px; color: #ffffff;
  }
  .legal {
    position: absolute; left: 66px; top: 352px;
    font-family: "Open Sans", sans-serif; font-size: 7px; line-height: 10px;
    color: var(--muted-ink);
  }
  .slide__footer-bar {
    position: absolute; left: 0; bottom: 0; width: 720px; height: 8px;
    background: var(--accent-yellow);
  }
</style>
</head>
<body>
<main class="canvas">

  <section class="slide slide--media">
    <svg class="slide__band" viewBox="0 0 720 320" role="img" aria-label="Hand holding floating media thumbnails over a dark grey band">
      <defs>
        <linearGradient id="mediaTone" x1="0" x2="1" y1="0" y2="0">
          <stop offset="0" stop-color="#b9c0cc"/>
          <stop offset="0.35" stop-color="#c9c6c4"/>
          <stop offset="0.55" stop-color="#7f8896"/>
          <stop offset="0.75" stop-color="#4a5361"/>
          <stop offset="1" stop-color="#4a5361"/>
        </linearGradient>
      </defs>
      <path d="M0 164 H300 C335 164 345 124 400 124 H720 V314 H0 Z" fill="url(#mediaTone)"/>
      <rect x="0" y="314" width="720" height="5" fill="var(--rule-grey)"/>
    </svg>
    <div class="brand"><span class="brand__dot"></span><span class="brand__name">NORTHPEAK</span></div>
    <div class="brand__sub">INTERACTIVE MEDIA</div>
    <div class="cover-title">
      <div class="cover-title__welcome">WELCOME</div>
      <div class="cover-title__sub">TO OUR PRESENTATION</div>
      <div class="cover-title__date">Birmingham, March 25, 2018</div>
    </div>
    <p class="legal">© 2017 All rights reserved. Contains confidential and proprietary information and may not be disclosed or<br>reproduced without the prior written consent of northpeak interactive media</p>
    <div class="slide__footer-bar"></div>
  </section>

  <section class="slide slide--touch">
    <svg class="slide__band" viewBox="0 0 720 320" role="img" aria-label="Finger touching a tablet with glowing digital icons over a dark grey band">
      <defs>
        <linearGradient id="touchTone" x1="0" x2="1" y1="0" y2="0">
          <stop offset="0" stop-color="#0d1626"/>
          <stop offset="0.25" stop-color="#1f4f86"/>
          <stop offset="0.45" stop-color="#8a8488"/>
          <stop offset="0.65" stop-color="#4a5361"/>
          <stop offset="1" stop-color="#4a5361"/>
        </linearGradient>
      </defs>
      <path d="M0 164 H300 C335 164 345 124 400 124 H720 V314 H0 Z" fill="url(#touchTone)"/>
      <rect x="0" y="314" width="720" height="5" fill="var(--rule-grey)"/>
    </svg>
    <div class="brand"><span class="brand__dot"></span><span class="brand__name">NORTHPEAK</span></div>
    <div class="brand__sub">INTERACTIVE MEDIA</div>
    <div class="cover-title">
      <div class="cover-title__welcome">WELCOME</div>
      <div class="cover-title__sub">TO OUR PRESENTATION</div>
      <div class="cover-title__date">Birmingham, March 25, 2018</div>
    </div>
    <p class="legal">© 2017 All rights reserved. Contains confidential and proprietary information and may not be disclosed or<br>reproduced without the prior written consent of northpeak interactive media</p>
    <div class="slide__footer-bar"></div>
  </section>

</main>
</body>
</html>
```